First North America Product Category Rule

8 x 10 foot booth design for a stretch fabric wrap-around. The booth will be used in a very small exhibit area for 150 attendees. It is for the packaging industry focused on the environment. This booth graphic is NOT about our company, but to promote participation in a project we are sponsoring. The project is to develop the first North American Packaging Category Rule, so the booth is to invite conference attendees to join our effort. Production specifications are attached.

Target Market(s)

Zenith 400, Sustainability Directors, Packaging Engineers

Industry/Entity Type

Packaging; Environment

Font styles to use
Sans Serif

Requirements
Must have
• An Eye-Catching or Intriguing Image/Graphics/Letter Treatment
Should not have
• Nothing too bright or garish. All text should be above waist height (No text below the 36-40" mark)

```html
<!DOCTYPE html>
<html lang="en">
<head>
<meta charset="utf-8">
<title>Product Category Rule for Protective Packaging – Booth Graphic</title>
<link href="https://fonts.googleapis.com/css2?family=Jost:wght@300;400;600;700&display=swap" rel="stylesheet">
<style>
  :root {
    --page-bg: #9fb0b3;
    --booth-blue: #12cdf6;
    --panel-white: #ffffff;
    --teal: #1a8fba;
    --tile-teal: #1b9cc6;
    --ribbon-top: #4ea9cf;
    --ribbon-bottom: #5a7fb0;
    --ink: #111111;
    --photo-dark: #3d3a38;
    --photo-warm: #8a6a4c;
    --vest-orange: #f4a72a;
    --skin: #d9b49a;
  }
  * { box-sizing: border-box; margin: 0; padding: 0; }
  html, body { width: 857px; height: 1200px; overflow: hidden; }
  body {
    background: var(--page-bg);
    font-family: "Jost", Arial, sans-serif;
    position: relative;
  }
  .booth {
    position: absolute;
    left: 20px; top: 370px;
    width: 817px; height: 461px;
    background: var(--booth-blue);
    overflow: hidden;
  }
  .info-panel {
    position: absolute;
    left: 135px; top: 17px;
    width: 547px; height: 247px;
    background: var(--panel-white);
  }
  .warehouse-photo {
    position: absolute;
    left: 135px; top: 264px;
    width: 547px; height: 180px;
    background: linear-gradient(90deg, var(--photo-dark) 0%, #55606a 30%, #6b6660 60%, var(--photo-warm) 100%);
  }
  .worker-portrait {
    position: absolute;
    left: 279px; top: 187px;
    width: 227px; height: 274px;
    border-radius: 90px 90px 0 0;
    background: linear-gradient(180deg, var(--vest-orange) 0%, var(--skin) 30%, var(--skin) 45%, var(--vest-orange) 60%, #e89a22 100%);
  }
  .eyebrow {
    position: absolute;
    left: 151px; top: 44px;
    font-size: 14px; font-weight: 700;
    color: var(--teal);
    letter-spacing: -0.2px;
  }
  .headline {
    position: absolute;
    left: 150px; top: 59px;
    font-size: 24.5px; font-weight: 300;
    line-height: 27px;
    color: var(--ink);
    letter-spacing: -0.6px;
    text-transform: uppercase;
  }
  .headline .acronym { color: var(--teal); }
  .subhead {
    position: absolute;
    left: 152px; top: 126px;
    font-size: 16.5px; font-weight: 700;
    color: var(--ink);
    letter-spacing: -0.2px;
  }
  .quote {
    position: absolute;
    left: 152px; top: 157px;
    width: 170px;
    font-size: 10.5px; font-weight: 600;
    line-height: 11.7px;
    color: var(--ink);
  }
  .signup-ribbon {
    position: absolute;
    left: 518px; top: 2px;
    width: 140px; height: 86px;
  }
  .signup-text {
    position: absolute;
    left: 524px; top: 17px;
    width: 130px;
    text-align: center;
    font-size: 21px; font-weight: 700;
    line-height: 20px;
    color: #ffffff;
  }
  .process-grid {
    position: absolute;
    left: 503px; top: 107px;
    width: 128px; height: 128px;
    display: grid;
    grid-template-columns: 1fr 1fr;
    grid-template-rows: 1fr 1fr;
    gap: 2px;
  }
  .process-step {
    background: var(--tile-teal);
    color: #ffffff;
    position: relative;
    font-size: 7.5px; font-weight: 300;
    line-height: 8.5px;
    text-align: center;
  }
  .process-step:nth-child(1) { border-radius: 10px 0 0 0; }
  .process-step:nth-child(2) { border-radius: 0 10px 0 0; }
  .process-step:nth-child(3) { border-radius: 0 0 0 10px; }
  .process-step:nth-child(4) { border-radius: 0 0 10px 0; }
  .step-label { position: absolute; left: 0; right: 0; }
  .step-top .step-label { top: 9px; }
  .step-bottom .step-label { top: 18px; }
  .step-number {
    position: absolute;
    font-size: 9px; font-weight: 700;
  }
  .step-top .step-number { bottom: 2px; }
  .step-bottom .step-number { top: 2px; }
  .step-left .step-number { right: 4px; }
  .step-right .step-number { left: 4px; }
  .sponsors {
    position: absolute;
    left: 480px; top: 238px;
    width: 174px;
    text-align: center;
    font-size: 8.3px; font-weight: 600;
    line-height: 10.5px;
    color: var(--teal);
  }
</style>
</head>
<body>
  <main class="booth">
    <div class="info-panel"></div>
    <div class="warehouse-photo" role="img" aria-label="Blurred warehouse aisle with shelving and a worker in a hi-vis vest"></div>
    <div class="worker-portrait" role="img" aria-label="Portrait of a packaging engineer in an orange hard hat and safety vest, arms crossed"></div>

    <p class="eyebrow">FIRST NORTH AMERICAN</p>
    <h1 class="headline">Product Category Rule <span class="acronym">(PCR)</span><br>for Protective Packaging</h1>
    <h2 class="subhead">ENLISTING STAKEHOLDER PARTICIPATION</h2>
    <p class="quote">“How EPD Can Move<br>the Dialogue Beyond<br>End-of-Life Disposal<br>to Include Environmental<br>Benchmarks for<br>Product Production<br>&amp; Distribution”</p>

    <svg class="signup-ribbon" viewBox="0 0 140 86" aria-hidden="true">
      <defs>
        <linearGradient id="ribbonFill" x1="0" y1="0" x2="0" y2="1">
          <stop offset="0" stop-color="var(--ribbon-top)"/>
          <stop offset="1" stop-color="var(--ribbon-bottom)"/>
        </linearGradient>
      </defs>
      <polygon points="0,10 6,0 6,10" fill="#3a6f92"/>
      <polygon points="140,10 134,0 134,10" fill="#3a6f92"/>
      <polygon points="6,0 134,0 134,60 70,82 6,60" fill="url(#ribbonFill)"/>
    </svg>
    <p class="signup-text">SIGN UP<br>NOW!</p>

    <div class="process-grid">
      <div class="process-step step-top step-left"><span class="step-label">PCR<br>Product<br>Category<br>Rules</span><span class="step-number">01</span></div>
      <div class="process-step step-top step-right"><span class="step-label">LCA<br>Life<br>Cycle<br>Assessment</span><span class="step-number">02</span></div>
      <div class="process-step step-bottom step-left"><span class="step-label">EPD<br>Registration<br>and<br>Publication</span><span class="step-number">04</span></div>
      <div class="process-step step-bottom step-right"><span class="step-label">Third<br>Party<br>Verification</span><span class="step-number">03</span></div>
    </div>

    <p class="sponsors">Sponsored by Foam Packaging Council<br>Managed by Clearpath Ledger</p>
  </main>
</body>
</html>
```